Website for Party

Design a new website for PlumtreeGatherings.net
We have attached the new logos and please look at the website, and our facebook page: facebook.com/plumtreegatherings for inspiration
Updates

Hi Guys, please be original with all designs and images otherwise the design will be eliminated Thank you

some of your designs have too much happening in them, others make it clear that the designer has not yet read the brief fully

Please everyone be original!

```html
<!DOCTYPE html>
<html lang="en">
<head>
<meta charset="utf-8">
<title>Plumtree Gatherings</title>
<link href="https://fonts.googleapis.com/css2?family=Open+Sans:wght@300;400;600;700&display=swap" rel="stylesheet">
<style>
:root{
  --ink:#0b0b10;
  --nav:#5a5a5e;
  --red:#e0252f;
  --red-dark:#b71a23;
  --white:#ffffff;
  --muted:#d6d6da;
  --tile-blue:rgba(30,70,140,.82);
  --tile-gold:rgba(150,110,60,.82);
  --tile-red:rgba(200,30,40,.85);
  --tile-purple:rgba(70,40,130,.82);
  --tile-orange:rgba(220,110,20,.85);
}
*{box-sizing:border-box;margin:0;padding:0}
html,body{width:793px;height:1200px;overflow:hidden;background:var(--ink)}
body{font-family:"Open Sans",Arial,sans-serif;color:var(--white);position:relative}

.night-sky{position:absolute;left:0;top:111px;width:793px;height:1089px;
  background:radial-gradient(circle at 15% 70%,rgba(200,40,80,.45),transparent 25%),
  radial-gradient(circle at 88% 60%,rgba(230,120,40,.4),transparent 22%),
  radial-gradient(circle at 20% 92%,rgba(90,60,200,.45),transparent 25%),
  radial-gradient(circle at 85% 95%,rgba(220,60,90,.4),transparent 22%),
  linear-gradient(#161018,#0a0a14 40%,#120c1c)}

.topbar{position:absolute;top:0;left:0;width:793px;height:74px;background:#0a0a0a;display:flex;align-items:center;justify-content:space-between;padding:0 58px 0 80px}
.brand{display:flex;align-items:center;gap:12px;font-size:30px;font-weight:600;letter-spacing:2px}
.brand-mark{width:30px;height:30px;border-radius:50%;background:var(--white)}
.social{display:flex;gap:6px}
.social span{width:18px;height:18px;background:#6b7fb0;border-radius:2px}
.social span:nth-child(2){background:#59a7d8}
.social span:nth-child(3){background:#4a6ea8}
.social span:nth-child(4){background:#c9342c}
.social span:nth-child(5){background:#777}
.social span:nth-child(6){background:#3b7dbf}
.social span:nth-child(7){background:#c42a2a}

.mainnav{position:absolute;top:74px;left:0;width:793px;height:37px;background:var(--nav);display:flex;align-items:center;padding-left:84px}
.mainnav a{color:var(--white);text-decoration:none;font-size:11px;font-weight:600;padding:0 15px;height:37px;line-height:37px}
.mainnav a.active{background:var(--red)}
.phone{margin-left:auto;padding-right:40px;font-size:22px;font-weight:300}
.phone b{font-weight:600}

.hero{position:absolute;top:111px;left:0;width:793px;height:320px;
  background:radial-gradient(circle at 25% 40%,rgba(220,170,110,.5),transparent 30%),
  radial-gradient(circle at 70% 45%,rgba(200,140,100,.45),transparent 28%),
  linear-gradient(#1a1420,#2a1d24 60%,rgba(20,14,22,0))}
.arrow{position:absolute;top:222px;width:22px;height:34px;background:var(--red);display:flex;align-items:center;justify-content:center}
.arrow.left{left:0}.arrow.right{right:0}

.signup{position:absolute;top:431px;left:74px;width:645px;height:40px;background:var(--red);display:flex;align-items:center;padding:0 10px;gap:10px;font-size:9px}
.signup input{width:210px;height:20px;border:0;font:9px "Open Sans",sans-serif;padding:0 6px;color:#999}
.signup button{height:20px;width:60px;background:var(--red-dark);color:var(--white);border:1px solid rgba(255,255,255,.5);font:700 9px "Open Sans",sans-serif}

.features{position:absolute;top:489px;left:79px;width:635px;display:grid;grid-template-columns:312px 312px;column-gap:11px;row-gap:14px}
.tile{height:148px;position:relative;overflow:hidden;display:flex}
.tile .photo{flex:0 0 45%}
.tile .copy{flex:1;padding:10px 12px}
.tile h2{font-size:19px;font-weight:300;line-height:1.15;margin-bottom:6px}
.tile h2 b{font-weight:600}
.tile p{font-size:7.5px;line-height:1.35;color:var(--muted)}
.tile.rev{flex-direction:row-reverse}

.blue .copy{background:var(--tile-blue)} .blue .photo{background:linear-gradient(135deg,#2a4f88,#8aa2c8)}
.gold .copy{background:var(--tile-gold)} .gold .photo{background:linear-gradient(135deg,#6a4a2a,#d9b27a)}
.red .copy{background:var(--tile-red)} .red .photo{background:linear-gradient(135deg,#3a0c10,#c52a32)}
.purple .copy{background:var(--tile-purple)} .purple .photo{background:linear-gradient(135deg,#281a60,#5c7ae0)}
.orange .copy{background:var(--tile-orange)} .orange .photo{background:linear-gradient(135deg,#e08a2a,#f0c060)}
.wine .copy{background:var(--tile-gold)} .wine .photo{background:linear-gradient(135deg,#e8d6b0,#9a1a24)}
.food .copy{background:var(--tile-orange)} .food .photo{background:linear-gradient(135deg,#8a3a12,#e09a40)}
.stage .copy{background:var(--tile-blue)} .stage .photo{background:linear-gradient(135deg,#3a2a40,#c08a70)}

.footer{position:absolute;top:1137px;left:0;width:793px;height:63px;display:flex;align-items:center;justify-content:space-between;padding:0 60px 0 18px}
.footnav a{color:var(--white);text-decoration:none;font-size:11px;font-weight:600;margin-right:12px}
.footnav small{display:block;font-size:7px;color:#aaa;margin-top:4px}
.footer .brand{font-size:24px;color:#ddd}
.footer .brand-mark{width:24px;height:24px;background:#ddd}
</style>
</head>
<body>
<div class="night-sky" role="img" aria-label="Fireworks bursting over a harbor skyline at night"></div>

<header class="topbar">
  <div class="brand"><span class="brand-mark"></span>Plumtree</div>
  <div class="social"><span></span><span></span><span></span><span></span><span></span><span></span><span></span></div>
</header>

<nav class="mainnav">
  <a class="active" href="#">WELCOME</a><a href="#">ABOUT</a><a href="#">FAQ</a><a href="#">ORDER TICKETS</a><a href="#">CONTACT US</a>
  <span class="phone">Phone: <b>123 456 7890</b></span>
</nav>

<section class="hero" role="img" aria-label="Guitarists performing live on a stage under warm lights"></section>
<span class="arrow left"><svg width="10" height="14"><path d="M8 1 2 7l6 6" stroke="#fff" stroke-width="2" fill="none"/></svg></span>
<span class="arrow right"><svg width="10" height="14"><path d="M2 1l6 6-6 6" stroke="#fff" stroke-width="2" fill="none"/></svg></span>

<form class="signup">
  <span>Enter your email address below to be added to our mailing list</span>
  <input type="text" value="Your email address here">
  <button type="button">SUBMIT</button>
</form>

<main class="features">
  <article class="tile blue">
    <div class="copy"><h2>3+ Hour Cruise around <b>NYC Harbor</b></h2><p>Board a beautiful cruise through the harbor as the skyline glows and the night begins with music, lights and good company.</p></div>
    <div class="photo" role="img" aria-label="Cruise ship on the harbor at dusk"></div>
  </article>
  <article class="tile stage rev">
    <div class="copy"><h2>Opening Performance by <b>Milo Ferrant</b></h2><p>Our opening act sets the tone with a live guitar set that warms up the crowd before the main celebration starts.</p></div>
    <div class="photo" role="img" aria-label="Musician playing guitar on stage"></div>
  </article>
  <article class="tile wine">
    <div class="copy"><h2>Open Premium <b>Bar</b></h2><p>Enjoy premium spirits, fine wines and crafted cocktails poured all night by our friendly team of skilled bartenders.</p></div>
    <div class="photo" role="img" aria-label="Glass of white wine"></div>
  </article>
  <article class="tile gold rev">
    <div class="copy"><h2>Hors d'oeuvres</h2><p>Passed bites and small plates from our chefs keep guests fed and happy while they mingle across the deck.</p></div>
    <div class="photo" role="img" aria-label="Plated appetizers"></div>
  </article>
  <article class="tile red">
    <div class="copy"><h2>Red Carpet <b>Entry</b></h2><p>Arrive in style and pose on the red carpet where our photographers capture every guest before boarding begins.</p></div>
    <div class="photo" role="img" aria-label="Guests arriving on a red carpet"></div>
  </article>
  <article class="tile purple rev">
    <div class="copy"><h2>Epic Mixes by <b>DJ Koval</b></h2><p>Dance until late as our resident DJ mixes the best hits and fresh tracks under the open night sky.</p></div>
    <div class="photo" role="img" aria-label="DJ booth with colorful stage lights"></div>
  </article>
  <article class="tile orange">
    <div class="copy"><h2>Personalized <b>Gift Bag</b></h2><p>Every guest leaves with a curated gift bag full of treats and keepsakes from the evening.</p></div>
    <div class="photo" role="img" aria-label="Wrapped gift bag"></div>
  </article>
  <article class="tile food rev">
    <div class="copy"><h2>Premium <b>Buffet</b></h2><p>A generous buffet with hot dishes, salads and desserts is served later in the night for all guests.</p></div>
    <div class="photo" role="img" aria-label="Buffet table with warm dishes"></div>
  </article>
</main>

<footer class="footer">
  <div class="footnav">
    <a href="#">WELCOME</a><a href="#">ABOUT</a><a href="#">FAQ</a><a href="#">ORDER TICKETS</a><a href="#">CONTACT US</a>
    <small>Copyright Plumtree</small>
  </div>
  <div class="brand"><span class="brand-mark"></span>Plumtree</div>
</footer>
</body>
</html>
```